Redesign criminal justice consulting website

We run a small professional services firm that does research, evaluation, consulting, and training on criminal justice issues. We need to redesign our website (www.rvmetrics.com). The existing site is something we made ourselves. It is unprofessional and does not do a good job of communicating what we do or who we are.

We would like the new site to provide a basic overview of what we do. Moreover, we would like it to communicate several themes that represent who we are:

* global

* innovative

* analytical

* practical

We view the principal design challenge as figuring out a subtle, interesting, and graphically appealing way to communicate these themes.

Target Market(s)

Our primary customers are governments, research firms, criminal justice agencies, and schools. The people who we want to find our site are seeking research, evaluation, training, or consulting services related to crime, criminal justice, or policing.

Industry/Entity Type

Consulting

Number of Pages Required

2 pages

Requirements
Must have
• 1. We would like the site to use our logo. It is attached (please use the maroon 4-color version with the company name but without the slogan). The site should also use the colors present in our logo. It may use other colors as well, as long as these colors coordinate with the logo colors.

• 2. For main pages or buttons, we need the following:
• *Home
• *About RVM
• *Services
• *E-Training
• *Resources
• *Contact RVM

• 3. We like simple, crisp, subtle designs over "busier," cluttered, or very complex designs.

• 4. We'd like to receive, at a minimum, the home page and a sample inner page.
Nice to have
• We need some help in thinking through what regions or sections should exist on the home page. We are thinking about having a window on there where we can make announcements about recent developments like new reports, new e-training videos, new photographs, etc... We are open to suggestions here.
Should not have
• 1. Gimmicky or overused clipart.
• 2. Cliched images associated with criminal justice, including magnifying glasses, scales of justice, etc... Our logo makes a subtle nod to criminal justice through the use of a fingerprint as the dot on the "J" in the company initials. That''s sufficient for our purposes. Concentrate instead on the themes listed above.
• 3. Major use of colors that don't match our logo, like blue.

```html
<!DOCTYPE html>
<html lang="en">
<head>
<meta charset="utf-8">
<title>RVM — Rivera Vance Metrics</title>
<link rel="stylesheet" href="https://fonts.googleapis.com/css2?family=Libre+Baskerville:wght@400;700&family=Open+Sans:wght@400;600;700&display=swap">
<style>
:root{
  --maroon:#8b0a0d;
  --maroon-deep:#5e0507;
  --maroon-mid:#a3161a;
  --cream:#f0e2cc;
  --sand:#e8d6b6;
  --sand-light:#f4ead9;
  --gold-top:#f5e4c2;
  --gold-bot:#dcbf8c;
  --ink:#1c1c1c;
  --grey:#9a9a9a;
  --rule:#e4d3b6;
}
*{margin:0;padding:0;box-sizing:border-box}
html,body{width:718px;height:1200px;overflow:hidden;background:#fff}
.canvas{position:absolute;left:0;top:0;width:1220px;height:2039px;transform:scale(0.5885);transform-origin:0 0;font-family:"Open Sans",Arial,sans-serif;color:var(--ink)}

.page-band{position:absolute;left:0;width:1220px;background:linear-gradient(90deg,#e6d2ae 0%,#f4ead9 11%,#f4ead9 89%,#e6d2ae 100%)}
.sheet{position:absolute;left:137px;width:950px;background:#fff}

.brand{position:absolute;display:flex;align-items:center;gap:12px}
.brand-dot{width:22px;height:22px;border-radius:50%;background:var(--maroon)}
.brand-name{font-family:"Libre Baskerville",Georgia,serif;font-weight:700;font-size:52px;color:var(--maroon);letter-spacing:1px}

.search-field{position:absolute;width:206px;height:23px;border:1px solid #555;background:#fff}
.search-btn{position:absolute;width:77px;height:25px;background:var(--maroon);color:#fff;font-family:"Libre Baskerville",Georgia,serif;font-weight:700;font-size:14px;text-align:center;line-height:25px}

.nav{position:absolute;left:137px;width:950px;height:38px}
.nav-item{position:absolute;top:0;height:38px;line-height:38px;font-family:"Libre Baskerville",Georgia,serif;font-weight:700;font-size:14px;color:var(--maroon);letter-spacing:.3px}
.nav-div{position:absolute;top:2px;width:1px;height:34px;background:var(--rule)}

.hero{position:absolute;left:137px;width:950px;background:linear-gradient(180deg,var(--maroon) 0%,#7d080b 60%,var(--maroon-deep) 100%)}
.hero-title{position:absolute;left:0;width:610px;text-align:center;font-family:"Libre Baskerville",Georgia,serif;font-size:45px;line-height:55px;color:var(--cream);letter-spacing:1px;font-weight:400}
.hero-rule{position:absolute;height:1px;background:#5a0407;box-shadow:0 1px 0 #9c2226}
.hero-copy{position:absolute;text-align:center;color:#fff;font-size:16.5px;line-height:22px}
.hero-btn{position:absolute;width:230px;height:44px;background:linear-gradient(180deg,var(--gold-top),var(--gold-bot));border:1px solid #f7ecd5;color:var(--maroon);font-family:"Libre Baskerville",Georgia,serif;font-weight:700;font-size:17px;text-align:center;line-height:42px}
.globe{position:absolute;border-radius:50%;background:radial-gradient(circle at 45% 40%,#a01217 0%,#6e0709 70%,#4a0305 100%);box-shadow:inset 0 0 0 2px #3d0204}
.globe-echo{position:absolute;border-radius:50% 50% 0 0;background:linear-gradient(180deg,rgba(70,3,5,.35),rgba(70,3,5,0))}

.section-title{position:absolute;font-family:"Libre Baskerville",Georgia,serif;font-size:23px;color:var(--maroon);font-weight:400}
.col-head{position:absolute;height:33px;border-top:1px solid #333;border-bottom:1px solid #333;font-family:"Libre Baskerville",Georgia,serif;font-size:16px;line-height:31px;color:#111}
.col-head .go{position:absolute;right:6px;top:7px}

.report{position:absolute;left:168px;width:362px}
.report-thumb{float:left;width:93px;height:71px;margin:3px 12px 0 1px;border:1px solid #ccc;background:linear-gradient(135deg,#fbfbfb 0%,#e8eef2 60%,#cfe0ea 100%)}
.report-title{font-size:16px;line-height:22px;color:var(--maroon);font-weight:400;margin-bottom:4px;white-space:nowrap}
.report-text{font-size:12.4px;line-height:17px;color:#222}
.report .more{position:static;display:block;clear:both;padding-top:14px}

.photo-blue{position:absolute;background:linear-gradient(135deg,#1d5fa6 0%,#6ea6d8 45%,#cfe2f2 70%,#2c73b8 100%)}
.photo-sky{position:absolute;background:linear-gradient(180deg,#b7c2cf 0%,#d2d7de 45%,#6f7c86 70%,#8a8f8c 100%)}
.photo-dusk{position:absolute;background:linear-gradient(180deg,#d9a9b6 0%,#e7b7a9 45%,#6b6450 75%,#4d4a34 100%)}
.photo-green{position:absolute;background:linear-gradient(180deg,#9aa692 0%,#6f8060 45%,#bfc3c3 75%,#dfe1e1 100%)}

.body{position:absolute;font-size:12.4px;line-height:17px;color:#222}
.caption{position:absolute;font-size:12.4px;line-height:17px;color:var(--maroon)}
.more{position:absolute;font-size:12.6px;font-weight:700;color:var(--maroon)}

.footer{position:absolute;left:170px;width:887px;height:90px;border:1px solid #ececec;background:linear-gradient(180deg,#eeeeee 0%,#fafafa 60%,#fff 100%);text-align:center;font-family:"Libre Baskerville",Georgia,serif;color:var(--grey)}
.footer-links{position:absolute;left:0;right:0;top:26px;font-size:12px;font-weight:700}
.footer-links span{font-weight:400;margin:0 6px}
.footer-copy{position:absolute;left:0;right:0;top:50px;font-size:11.5px}

.svc-hero-title{position:absolute;font-family:"Libre Baskerville",Georgia,serif;font-size:29px;color:var(--cream);letter-spacing:1px;font-weight:400}
.svc-hero-copy{position:absolute;font-size:12.4px;line-height:17px;color:#fff}
.svc-intro{position:absolute;font-family:"Libre Baskerville",Georgia,serif;font-size:16.6px;line-height:22px;color:#111;letter-spacing:-.1px}
.svc-head{position:absolute;font-size:16px;line-height:21px;color:var(--maroon);font-weight:400}
.svc-div{position:absolute;width:1px;background:linear-gradient(180deg,rgba(228,211,182,0),var(--rule) 20%,var(--rule) 80%,rgba(228,211,182,0))}
.svc-list{list-style:none}
</style>
</head>
<body>
<div class="canvas">

  <!-- ===== Home page ===== -->
  <div class="page-band" style="top:95px;height:987px"></div>
  <div class="brand" style="left:168px;top:28px"><span class="brand-dot"></span><span class="brand-name">RVM</span></div>
  <div class="search-field" style="left:797px;top:59px"></div>
  <div class="search-btn" style="left:1010px;top:58px">Search</div>

  <nav class="nav" style="top:98px">
    <span class="nav-item" style="left:33px">HOME</span>
    <span class="nav-div" style="left:120px"></span>
    <span class="nav-item" style="left:159px">ABOUT RVM</span>
    <span class="nav-div" style="left:281px"></span>
    <span class="nav-item" style="left:323px">SERVICES</span>
    <span class="nav-div" style="left:434px"></span>
    <span class="nav-item" style="left:475px">E-TRAINING</span>
    <span class="nav-div" style="left:606px"></span>
    <span class="nav-item" style="left:647px">RESOURCES</span>
    <span class="nav-div" style="left:777px"></span>
    <span class="nav-item" style="left:815px">CONTACT RVM</span>
  </nav>

  <section class="hero" style="top:137px;height:363px">
    <h1 class="hero-title" style="top:36px">INNOVATIONS IN<br>CRIME PREVENTION</h1>
    <div class="hero-rule" style="left:118px;top:163px;width:376px"></div>
    <p class="hero-copy" style="left:60px;top:192px;width:470px">We specialize in working closely with our clients to design tailored, innovative solutions.<br>Call today and explore how we can be of service.</p>
    <div class="hero-btn" style="left:184px;top:281px">CONTACT RVM</div>
    <div class="globe" role="img" aria-label="Globe assembled from interlocking puzzle pieces" style="left:626px;top:24px;width:250px;height:250px"></div>
    <div class="globe-echo" role="img" aria-label="Faint reflection of the puzzle globe" style="left:646px;top:276px;width:210px;height:87px"></div>
  </section>

  <div class="sheet" style="top:500px;height:582px"></div>
  <h2 class="section-title" style="left:169px;top:519px">OUR RECENT DEVELOPMENTS</h2>

  <div class="col-head" style="left:167px;top:571px;width:370px">REPORTS
    <svg class="go" width="20" height="20" viewBox="0 0 20 20"><circle cx="10" cy="10" r="9" fill="var(--maroon)"/><path d="M5 10h8M10 6l4 4-4 4" stroke="#fff" stroke-width="2" fill="none"/></svg></div>
  <div class="col-head" style="left:561px;top:571px;width:228px">E-TRAINING VIDEOS
    <svg class="go" width="20" height="20" viewBox="0 0 20 20"><circle cx="10" cy="10" r="9" fill="var(--maroon)"/><path d="M5 10h8M10 6l4 4-4 4" stroke="#fff" stroke-width="2" fill="none"/></svg></div>
  <div class="col-head" style="left:817px;top:571px;width:241px">PHOTOGRAPHS
    <svg class="go" width="20" height="20" viewBox="0 0 20 20"><circle cx="10" cy="10" r="9" fill="var(--maroon)"/><path d="M5 10h8M10 6l4 4-4 4" stroke="#fff" stroke-width="2" fill="none"/></svg></div>

  <!-- reports -->
  <article class="report" style="top:611px">
    <div class="report-thumb" role="img" aria-label="Rising red arrow over a field of blue arrows"></div>
    <h3 class="report-title">Lorem ipsum dolor sit amet.</h3>
    <p class="report-text">Lorem ipsum dolor sit amet, consectetur adipiscing elit. Praesent eget tortor tellus. Donec eu dui at mi suscipit lobortis. Etiam sed justo turpis, pellentesque venenatis nisl. In iaculis adipiscing mauris, id congue massa consectetur sed.</p>
    <span class="more">Read more &gt;&gt;</span>
  </article>

  <article class="report" style="top:776px">
    <div class="report-thumb" role="img" aria-label="Rising red arrow over a field of blue arrows"></div>
    <h3 class="report-title">Lorem ipsum dolor sit amet.</h3>
    <p class="report-text">Lorem ipsum dolor sit amet, consectetur adipiscing elit. Praesent eget tortor tellus. Donec eu dui at mi suscipit lobortis. Etiam sed justo turpis, pellentesque venenatis nisl. In iaculis adipiscing mauris, id congue massa consectetur sed.</p>
    <span class="more">Read more &gt;&gt;</span>
  </article>

  <!-- videos -->
  <div class="photo-blue" role="img" aria-label="Video still: hand with pen reviewing a chart" style="left:572px;top:615px;width:207px;height:114px"></div>
  <p class="caption" style="left:571px;top:735px;width:215px">Lorem ipsum dolor sit amet, conse ctetur adipiscing elit.</p>
  <div class="photo-blue" role="img" aria-label="Video still: hand with pen reviewing a chart" style="left:570px;top:780px;width:207px;height:114px"></div>
  <p class="caption" style="left:570px;top:903px;width:215px">Lorem ipsum dolor sit amet, conse ctetur adipiscing elit.</p>

  <!-- photographs -->
  <div class="photo-sky" role="img" aria-label="Waterfront pier under a cloudy sky" style="left:819px;top:615px;width:111px;height:73px"></div>
  <div class="photo-dusk" role="img" aria-label="Harbour shoreline at sunset" style="left:946px;top:615px;width:111px;height:73px"></div>
  <div class="photo-green" role="img" aria-label="Campus entrance sign with trees" style="left:819px;top:705px;width:111px;height:73px"></div>
  <div class="photo-sky" role="img" aria-label="Waterfront pier under a cloudy sky" style="left:946px;top:705px;width:111px;height:73px"></div>
  <div class="photo-dusk" role="img" aria-label="Harbour shoreline at sunset" style="left:819px;top:796px;width:111px;height:73px"></div>
  <div class="photo-green" role="img" aria-label="Campus entrance sign with trees" style="left:946px;top:796px;width:111px;height:73px"></div>

  <footer class="footer" style="top:993px">
    <div class="footer-links">Home<span>|</span>About RVM<span>|</span>Copyright Information<span>|</span>Privacy Policy<span>|</span>Contact RVM</div>
    <div class="footer-copy">Copyright 2010, Rivera Vance Metrics, Inc. All Rights Reserved.</div>
  </footer>

  <!-- ===== Services page ===== -->
  <div class="page-band" style="top:1213px;height:826px"></div>
  <div class="brand" style="left:168px;top:1146px"><span class="brand-dot"></span><span class="brand-name">RVM</span></div>
  <div class="search-field" style="left:797px;top:1177px"></div>
  <div class="search-btn" style="left:1010px;top:1176px">Search</div>

  <nav class="nav" style="top:1216px">
    <span class="nav-item" style="left:33px">HOME</span>
    <span class="nav-div" style="left:120px"></span>
    <span class="nav-item" style="left:159px">ABOUT RVM</span>
    <span class="nav-div" style="left:284px"></span>
    <span class="nav-item" style="left:323px">SERVICES</span>
    <span class="nav-div" style="left:437px"></span>
    <span class="nav-item" style="left:475px">E-TRAINING</span>
    <span class="nav-div" style="left:609px"></span>
    <span class="nav-item" style="left:647px">RESOURCES</span>
    <span class="nav-div" style="left:780px"></span>
    <span class="nav-item" style="left:815px">CONTACT RVM</span>
  </nav>

  <section class="hero" style="top:1253px;height:178px">
    <h1 class="svc-hero-title" style="left:32px;top:22px">SERVICES</h1>
    <p class="svc-hero-copy" style="left:34px;top:71px;width:885px">RVM specializes in offering a suite of related services to its clients. A common trajectory is for RVM to conduct an initial study or needs assessment, make a series of recommendations, work closely with agency staff to implement those recommendations, provide training and technical assistance throughout the implementation process, and then evaluate the success of the initiative. The results of the evaluation are then used to inform current practices and adjust strategic planning efforts. We believe this ongoing circular process of analysis, implementation, and evaluation is vital for transforming organizations and systems.</p>
  </section>

  <div class="sheet" style="top:1431px;height:608px"></div>
  <p class="svc-intro" style="left:172px;top:1476px;width:890px">RVM's four core practice areas reflect our underlying belief in the analytical process necessary for transforming organizations and systems.</p>

  <div class="svc-div" style="left:372px;top:1565px;height:290px"></div>
  <div class="svc-div" style="left:609px;top:1565px;height:290px"></div>
  <div class="svc-div" style="left:866px;top:1565px;height:290px"></div>

  <h3 class="svc-head" style="left:170px;top:1563px">Research, Evaluation,<br>&amp; Assessment</h3>
  <p class="body" style="left:171px;top:1615px;width:190px">RVM has considerable expertise in research, evaluation, and assessment using a variety of qualitative and quantitative methods.</p>
  <div class="more" style="left:172px;top:1720px">Learn more &gt;&gt;</div>

  <h3 class="svc-head" style="left:391px;top:1563px">Strategic Planning</h3>
  <p class="body" style="left:392px;top:1615px;width:208px">Today's criminal justice systems are complex and dynamic entities that rely on multiple agencies with different capacities and goals, personnel from various professional and personal backgrounds, and rapidly emerging changes in technology and tools.</p>
  <div class="more" style="left:393px;top:1790px">Learn more &gt;&gt;</div>

  <h3 class="svc-head" style="left:628px;top:1563px">Training</h3>
  <p class="body" style="left:628px;top:1618px;width:210px">We have provided training on a variety of topics, including those listed below:</p>
  <ul class="body svc-list" style="left:636px;top:1685px;width:225px">
    <li>- Strategic crime control</li>
    <li>- Criminal investigations</li>
    <li>- Crime analysis</li>
    <li>- Intelligence analysis</li>
    <li>- Crime prevention</li>
    <li>- Community policing</li>
    <li>- Problem-oriented policing</li>
    <li>- Addressing gang &amp; gun violence</li>
  </ul>
  <div class="more" style="left:628px;top:1845px">Learn more &gt;&gt;</div>

  <h3 class="svc-head" style="left:882px;top:1563px">Technical Assistance</h3>
  <p class="body" style="left:882px;top:1618px;width:182px">Sometimes training alone is not enough. Agencies can benefit from onsite coaching or technical assistance on a variety of issues. Our team of experts can provide various forms of technical assistance ranging from brief or periodic onsite assessment and coaching to implanting experts full-time in your agency.</p>
  <div class="more" style="left:882px;top:1845px">Learn more &gt;&gt;</div>

  <footer class="footer" style="top:1945px">
    <div class="footer-links">Home<span>|</span>About RVM<span>|</span>Copyright Information<span>|</span>Privacy Policy<span>|</span>Contact RVM</div>
    <div class="footer-copy">Copyright 2010, Rivera Vance Metrics, Inc. All Rights Reserved.</div>
  </footer>

</div>
</body>
</html>
```